Bully breed rescue website

I need a website for my bully breed rescue. We rescue bully breeds from up and down the east coast of the United States and train them as service dogs for people with limited mobility disabilities. I don't want a lot of white space. I want it to be modern and slick and colorful and still look professional. I want it to be different and have a lot of wow factor. I linked a copy of my logo.

Number of Pages Required

5+ page

Font styles to use
Sans Serif

Colors

Designer to choose colors to be used in the design.

Requirements
Must have
• Moving aspects. Blog and ecommerce.
• 1.) Home page
• 2.) Services- something modular
• 3.) About US
• 4.) Blog
• 5.) Application page
• 6.) Donation page
• 7.) Contact Us
Nice to have
• Large Slider of photos on home page
• vertical menu bar
Should not have
• Lots of white space. Dont want it to look like a template or any other site

```html
<!DOCTYPE html>
<html lang="en">
<head>
<meta charset="utf-8">
<title>Stand Tall Rescue</title>
<link rel="stylesheet" href="https://fonts.googleapis.com/css2?family=Montserrat:wght@400;600;700;800&family=Open+Sans:wght@400;600&display=swap">
<style>
:root{
  --yellow:#f7c20c;
  --yellow-deep:#e0a800;
  --red:#e4172e;
  --black:#0d0d0d;
  --charcoal:#262626;
  --grey-bg:#f0eeec;
  --white:#ffffff;
  --ink:#1a1a1a;
  --grey-btn:#8c8c8c;
}
*{box-sizing:border-box;margin:0;padding:0}
html,body{width:1200px;height:3782px;overflow:hidden}
body{font-family:"Open Sans",Arial,sans-serif;color:var(--ink);background:var(--white);position:relative}
.head{font-family:"Montserrat",Arial,sans-serif}
section,header,footer{position:absolute;left:0;width:1200px}
.abs{position:absolute}

/* Hero */
.hero{top:0;height:630px;overflow:hidden}
.hero-photo{position:absolute;inset:0;background:radial-gradient(ellipse at 62% 40%,#b7794a 0%,#8a5a33 25%,#5c4a2c 50%,#3a3322 80%,#2a2518 100%)}
.brand{left:76px;top:72px;display:flex;align-items:center;gap:12px;font-family:"Montserrat",sans-serif;font-weight:800;font-size:26px;color:var(--white);text-transform:uppercase}
.brand .dot{width:22px;height:22px;border-radius:50%;background:var(--yellow)}
.nav{left:350px;top:12px;display:flex;align-items:center;gap:10px;font-family:"Montserrat",sans-serif;font-size:13px;color:var(--white)}
.nav a{color:var(--white);text-decoration:none;padding:4px 10px}
.nav a.active{background:var(--yellow);color:var(--ink)}
.nav .phone{display:flex;align-items:center;gap:8px;font-weight:700;font-size:16px;margin-left:14px}
.cart{left:1076px;top:0;width:98px;height:45px;background:var(--white);display:flex;align-items:center;justify-content:center;gap:6px;font-family:"Montserrat",sans-serif;font-size:10px;color:var(--ink)}
.hero-title{left:108px;top:326px;font-family:"Montserrat",sans-serif;font-weight:800;font-size:48px;line-height:55px;color:var(--white);text-transform:uppercase}
.dots{left:565px;top:564px;display:flex;gap:14px}
.dots span{width:10px;height:10px;border-radius:50%;background:rgba(255,255,255,.6)}
.dots span.on{background:var(--white)}

/* Mission */
.mission{top:630px;height:562px;background:var(--black);overflow:hidden}
.mission-photo{position:absolute;inset:0;background:radial-gradient(ellipse at 60% 55%,#2d2d2d 0%,#161616 45%,#080808 100%)}
.mission-name{left:194px;top:100px;font-family:"Montserrat",sans-serif;font-weight:800;font-size:48px;color:var(--white)}
.mission h2{left:194px;top:206px;font-family:"Montserrat",sans-serif;font-weight:600;font-size:26px;color:var(--white)}
.mission p{left:194px;top:250px;width:480px;font-size:13px;line-height:21px;color:#e6e6e6}
.btn{display:inline-flex;align-items:center;justify-content:center;font-family:"Montserrat",sans-serif;font-weight:700;text-transform:uppercase;color:var(--white)}
.mission .btns{left:198px;top:408px;display:flex;gap:11px}
.mission .btns .btn{width:130px;height:41px;font-size:15px}
.btn.yellow{background:var(--yellow);color:var(--ink)}
.btn.red{background:var(--red)}
.btn.grey{background:var(--grey-btn)}

/* Features */
.features{top:1192px;height:912px;background:var(--grey-bg)}
.card{top:43px;width:345px;height:388px;text-align:center;color:var(--white)}
.card.services{left:60px;background:var(--yellow-deep)}
.card.about{left:423px;background:var(--charcoal)}
.card.merch{left:786px;background:var(--red)}
.card .icon{width:70px;height:70px;margin:75px auto 0;border-radius:8px;background:rgba(255,255,255,.2)}
.card h3{margin-top:18px;font-family:"Montserrat",sans-serif;font-weight:800;font-size:22px;text-transform:uppercase;color:var(--ink)}
.card.about h3,.card.merch h3{color:var(--white)}
.card p{width:240px;margin:12px auto 0;font-size:13px;line-height:20px}
.card .more{margin-top:22px;display:inline-block;border:2px solid var(--white);padding:6px 14px;font-family:"Montserrat",sans-serif;font-weight:700;font-size:10px;text-transform:uppercase}
.banner{left:60px;top:459px;width:1070px;height:398px;overflow:hidden}
.banner-photo{position:absolute;inset:0;background:linear-gradient(90deg,#3b3a2a 0%,#4a4630 40%,#6d5a3c 65%,#8e6a48 80%,#5a4a34 100%)}
.banner h2{left:74px;top:105px;width:520px;font-family:"Montserrat",sans-serif;font-weight:800;font-size:31px;line-height:33px;color:var(--white);text-transform:uppercase}
.banner .btn{left:76px;top:231px;width:207px;height:51px;font-size:18px;position:absolute}

/* Blog */
.blog{top:2104px;height:688px;background:var(--white)}
.section-title{width:100%;text-align:center;font-family:"Montserrat",sans-serif;font-weight:800;font-size:22px;text-transform:uppercase}
.blog .section-title{position:absolute;top:70px}
.post{top:164px;width:346px;height:424px}
.post .photo{width:346px;height:227px}
.post .box{position:absolute;left:20px;top:227px;width:306px;height:196px;background:var(--yellow);padding:26px 32px 0 34px;box-shadow:0 4px 10px rgba(0,0,0,.15)}
.post h3{font-family:"Montserrat",sans-serif;font-weight:800;font-size:15px;line-height:17px;text-transform:uppercase}
.post p{margin-top:12px;font-size:11px;line-height:15px}
.post .read{margin-top:18px;display:inline-block;background:var(--white);padding:5px 12px;font-family:"Montserrat",sans-serif;font-weight:700;font-size:10px;text-transform:uppercase}

/* Products */
.products{top:2792px;height:592px;background:var(--charcoal)}
.products .section-title{position:absolute;top:74px;color:var(--white)}
.product{top:159px;width:222px;height:353px;background:var(--white);text-align:center}
.product .shot{width:152px;height:190px;margin:35px auto 0;border-radius:6px}
.product h4{margin-top:30px;font-family:"Montserrat",sans-serif;font-weight:700;font-size:12px;text-transform:uppercase}
.product .price{margin-top:4px;font-family:"Montserrat",sans-serif;font-weight:600;font-size:20px}
.product .add{margin-top:10px;display:inline-block;background:var(--yellow);padding:5px 14px;font-family:"Montserrat",sans-serif;font-weight:700;font-size:10px;text-transform:uppercase}

/* Footer */
.footer{top:3384px;height:398px;background:var(--yellow)}
.footer-brand{left:113px;top:128px;display:flex;align-items:center;gap:14px;font-family:"Montserrat",sans-serif;font-weight:800;font-size:30px;color:var(--ink)}
.footer-brand .dot{width:26px;height:26px;border-radius:50%;background:var(--red)}
.col{top:78px;font-size:12px;line-height:19px}
.col h5{font-family:"Montserrat",sans-serif;font-weight:700;font-size:12px;text-transform:uppercase;margin-bottom:14px}
.contact-row{display:flex;align-items:flex-start;gap:12px;margin-bottom:16px}
.social{display:flex;align-items:center;gap:10px;margin-bottom:14px}
.social span.c{width:26px;height:26px;border-radius:50%;background:#1d3a6e}
.rule{left:113px;top:3692px;width:974px;height:1px;background:rgba(0,0,0,.15)}
.copy{top:332px;width:100%;text-align:center;font-size:11px}
</style>
</head>
<body>

<header class="hero">
  <div class="hero-photo" role="img" aria-label="Photo of a happy brown bully breed dog lying on autumn leaves"></div>
  <div class="abs brand"><span class="dot"></span>Stand Tall Rescue</div>
  <nav class="abs nav">
    <a class="active" href="#">Home</a><a href="#">Services</a><a href="#">About us</a><a href="#">Blog</a><a href="#">Application</a><a href="#">Donation</a><a href="#">Contact us</a>
    <span class="phone"><svg width="14" height="14" viewBox="0 0 24 24"><path fill="#fff" d="M6.6 10.8a15 15 0 0 0 6.6 6.6l2.2-2.2a1 1 0 0 1 1-.25 11.4 11.4 0 0 0 3.6.57 1 1 0 0 1 1 1V20a1 1 0 0 1-1 1A17 17 0 0 1 3 4a1 1 0 0 1 1-1h3.5a1 1 0 0 1 1 1c0 1.25.2 2.45.57 3.57a1 1 0 0 1-.25 1z"/></svg>555.014.2290</span>
  </nav>
  <div class="abs cart"><svg width="14" height="14" viewBox="0 0 24 24"><path fill="none" stroke="#1a1a1a" stroke-width="2" d="M3 4h3l2 11h11l2-8H7"/><circle cx="10" cy="19" r="1.5"/><circle cx="17" cy="19" r="1.5"/></svg>My Cart (0)</div>
  <h1 class="abs hero-title">Savings dogs<br>so they can<br>save us.</h1>
  <div class="abs dots"><span></span><span></span><span class="on"></span><span></span><span></span></div>
</header>

<section class="mission">
  <div class="mission-photo" role="img" aria-label="Dark photo of a bully breed dog running"></div>
  <div class="abs mission-name">Stand Tall Rescue</div>
  <h2 class="abs">OUR MISSION</h2>
  <p class="abs">But I must explain to you how all this mistaken idea of denouncing pleasure and praising pain was born and I will give you a complete account of the system, and expound the actual teachings of the great explorer of the truth, the master-builder of human happiness. No one rejects, dislikes, or avoids pleasure itself, because it is pleasure but because those who do not know how to pursue pleasure rationally encounter consequences.</p>
  <div class="abs btns"><span class="btn yellow">Blog</span><span class="btn red">Application</span><span class="btn grey">Donate</span></div>
</section>

<section class="features">
  <div class="abs card services">
    <div class="icon" role="img" aria-label="Sitting dog icon"></div>
    <h3>Services</h3>
    <p>But I must explain to you how all this mistaken idea of denouncing pleasure and praising pain.</p>
    <span class="more">Read more</span>
  </div>
  <div class="abs card about">
    <div class="icon" role="img" aria-label="Heart emblem icon"></div>
    <h3>About us</h3>
    <p>But I must explain to you how all this mistaken idea of denouncing pleasure and praising pain.</p>
    <span class="more">Read more</span>
  </div>
  <div class="abs card merch">
    <div class="icon" role="img" aria-label="Person walking a dog icon"></div>
    <h3>Merch</h3>
    <p>But I must explain to you how all this mistaken idea of denouncing pleasure and praising pain.</p>
    <span class="more">Read more</span>
  </div>
  <div class="abs banner">
    <div class="banner-photo" role="img" aria-label="Photo of a brown and white bully breed dog lying on grass"></div>
    <h2 class="abs">Lorem ipsum is simply dummy text of the printing</h2>
    <span class="btn red">Donate now</span>
  </div>
</section>

<section class="blog">
  <h2 class="section-title">Latest blog</h2>
  <article class="abs post" style="left:60px">
    <div class="photo" role="img" aria-label="Photo of a black dog standing in a park" style="background:linear-gradient(160deg,#8a8a86,#55564f 55%,#3d3f35)"></div>
    <div class="box"><h3>Lorem ipsum is simply dummy text of the</h3><p>Contrary to popular belief, Lorem Ipsum is not simply random text. It has roots in a piece of classical Lati</p><span class="read">Read more</span></div>
  </article>
  <article class="abs post" style="left:436px">
    <div class="photo" role="img" aria-label="Photo of a brindle and white dog outdoors" style="background:linear-gradient(160deg,#7a5a3c,#4c3426 55%,#6b4a30)"></div>
    <div class="box"><h3>Lorem ipsum is simply dummy text of the</h3><p>Contrary to popular belief, Lorem Ipsum is not simply random text. It has roots in a piece of classical Lati</p><span class="read">Read more</span></div>
  </article>
  <article class="abs post" style="left:809px">
    <div class="photo" role="img" aria-label="Photo of a dog lying in green grass" style="background:linear-gradient(160deg,#7fa046,#5b7d2e 55%,#4a6b28)"></div>
    <div class="box"><h3>Lorem ipsum is simply dummy text of the</h3><p>Contrary to popular belief, Lorem Ipsum is not simply random text. It has roots in a piece of classical Lati</p><span class="read">Read more</span></div>
  </article>
</section>

<section class="products">
  <h2 class="section-title">Products we use</h2>
  <div class="abs product" style="left:134px"><div class="shot" role="img" aria-label="Bag of dog treats" style="background:#2f9fb8"></div><h4>Lorem ipsum</h4><div class="price">$ 125.99</div><span class="add">Add to cart</span></div>
  <div class="abs product" style="left:373px"><div class="shot" role="img" aria-label="Bag of dog biscuits" style="background:#e0a21e"></div><h4>Lorem ipsum</h4><div class="price">$ 125.99</div><span class="add">Add to cart</span></div>
  <div class="abs product" style="left:607px"><div class="shot" role="img" aria-label="Can of pet food" style="background:#a9a9a9"></div><h4>Lorem ipsum</h4><div class="price">$ 125.99</div><span class="add">Add to cart</span></div>
  <div class="abs product" style="left:844px"><div class="shot" role="img" aria-label="Pouch of dog snacks" style="background:#c9b28a"></div><h4>Lorem ipsum</h4><div class="price">$ 125.99</div><span class="add">Add to cart</span></div>
</section>

<footer class="footer">
  <div class="abs footer-brand"><span class="dot"></span>Stand Tall Rescue</div>
  <div class="abs col" style="left:494px">
    <h5>Contact us</h5>
    <div class="contact-row"><svg width="12" height="14" viewBox="0 0 24 28"><path fill="#1a1a1a" d="M12 0a10 10 0 0 0-10 10c0 7.5 10 18 10 18s10-10.5 10-18A10 10 0 0 0 12 0zm0 14a4 4 0 1 1 0-8 4 4 0 0 1 0 8z"/></svg><span>48 Harbor Lane<br>Millbrook, ST 00421</span></div>
    <div class="contact-row"><svg width="13" height="13" viewBox="0 0 24 24"><path fill="#1a1a1a" d="M6.6 10.8a15 15 0 0 0 6.6 6.6l2.2-2.2a1 1 0 0 1 1-.25 11.4 11.4 0 0 0 3.6.57 1 1 0 0 1 1 1V20a1 1 0 0 1-1 1A17 17 0 0 1 3 4a1 1 0 0 1 1-1h3.5a1 1 0 0 1 1 1c0 1.25.2 2.45.57 3.57a1 1 0 0 1-.25 1z"/></svg><span>555.014.2291</span></div>
    <div class="contact-row"><svg width="14" height="11" viewBox="0 0 24 18"><rect x="1" y="1" width="22" height="16" fill="none" stroke="#1a1a1a" stroke-width="2"/><path d="M1 1l11 9 11-9" fill="none" stroke="#1a1a1a" stroke-width="2"/></svg><span>hello@standtallrescue.org</span></div>
  </div>
  <div class="abs col" style="left:751px">
    <h5>Menu</h5>
    Home<br>Services<br>About us<br>Blog<br>Application<br>Donation<br>Contact us
  </div>
  <div class="abs col" style="left:953px">
    <h5>Connect with us</h5>
    <div class="social"><span class="c"></span>Fanpage</div>
    <div class="social"><span class="c"></span>Updates</div>
    <div class="social"><span class="c"></span>Network</div>
  </div>
  <div class="abs copy">Copyrights @ 2018 All Rights Reserved</div>
</footer>
<div class="abs rule"></div>

</body>
</html>
```